依頼概要
200g〜1kgの瓶に詰めた日本蜂蜜のはちみつのシールデザインを募集します。
よくあるコテコテの感じよりは、少し変わったデザインを募集します。
一般に売られているはちみつよりも希少価値が高いはちみつです。
よろしくお願いします。
■ 選んだ理由

日本蜜蜂のはちみつの希少価値とデザインが合っていると思ったため。

■ 提案者全員のお礼・コメント

ご提案いただいた皆様、どうもありがとうございます。様々なデザインから選択するのは悩みましたが、希望に叶うものがあり大変嬉しく思います。
また何かあれば募集しますので、どうぞよろしくお願いします。

```html
<!DOCTYPE html>
<html lang="ja">
<head>
<meta charset="utf-8">
<title>Golden Reserve Honey – Label</title>
<link href="https://fonts.googleapis.com/css2?family=Cinzel:wght@700&family=Great+Vibes&family=Noto+Serif+JP:wght@700&family=Playfair+Display:ital@1&display=swap" rel="stylesheet">
<style>
  :root {
    --page: #ffffff;
    --panel-black: #0d0b08;
    --gold: #c9a24a;
    --gold-light: #ecd28c;
    --cream: #f7ecc4;
    --pattern-pink: #f3a9c8;
    --pattern-yellow: #f9e27a;
    --pattern-orange: #f7b76a;
    --pattern-green: #c9e08a;
    --pattern-lilac: #d9b4e6;
  }
  html, body {
    margin: 0;
    width: 1200px;
    height: 2284px;
    overflow: hidden;
    background: var(--page);
  }
  .canvas {
    position: relative;
    width: 1200px;
    height: 2284px;
  }
  .label {
    position: absolute;
    left: 120px;
    top: 862px;
    width: 960px;
    height: 560px;
    overflow: hidden;
    box-shadow: 0 0 0 1px #e6dcc8;
  }
  .label__pattern {
    position: absolute;
    inset: 0;
    background:
      radial-gradient(circle at 15% 20%, var(--pattern-pink) 0, transparent 40%),
      radial-gradient(circle at 85% 25%, var(--pattern-green) 0, transparent 38%),
      radial-gradient(circle at 20% 85%, var(--pattern-orange) 0, transparent 40%),
      radial-gradient(circle at 80% 80%, var(--pattern-lilac) 0, transparent 40%),
      var(--pattern-yellow);
    opacity: 0.85;
  }
  .panel {
    position: absolute;
    left: 184px;
    top: 28px;
    width: 328px;
    height: 464px;
    left: calc(50% - 164px);
    background: var(--panel-black);
    border: 5px solid var(--gold);
    box-shadow: inset 0 0 0 4px var(--panel-black), inset 0 0 0 6px var(--gold-light);
    box-sizing: border-box;
    display: flex;
    flex-direction: column;
    align-items: center;
    overflow: hidden;
  }
  .panel__emblem {
    margin-top: 22px;
    width: 44px;
    height: 44px;
    border-radius: 50%;
    background: var(--gold);
    flex: none;
  }
  .product-name {
    margin: 12px 0 0;
    text-align: center;
    color: var(--gold);
    font-family: "Cinzel", serif;
    font-weight: 700;
    line-height: 1;
  }
  .product-name__line {
    display: block;
    font-size: 46px;
    letter-spacing: 1px;
  }
  .product-name__script {
    display: block;
    margin-top: 2px;
    font-family: "Great Vibes", cursive;
    font-weight: 400;
    font-size: 50px;
    line-height: 1;
    color: var(--gold-light);
  }
  .jp-name {
    margin-top: 8px;
    width: 100%;
    padding: 8px 0 10px;
    border-top: 2px solid var(--gold);
    border-bottom: 2px solid var(--gold);
    text-align: center;
    color: var(--gold-light);
    font-family: "Noto Serif JP", serif;
    font-weight: 700;
    font-size: 36px;
    line-height: 1.2;
    letter-spacing: 3px;
  }
  .tagline {
    flex: 1;
    width: 100%;
    color: var(--cream);
    font-family: "Playfair Display", serif;
    font-style: italic;
    font-size: 19px;
    line-height: 1.3;
    text-align: center;
    display: flex;
    flex-direction: column;
    justify-content: center;
  }
  .tagline p { margin: 0; }
</style>
</head>
<body>
<main class="canvas">
  <section class="label">
    <div class="label__pattern" role="img" aria-label="Pastel pattern of colourful fan-shaped leaves in pink, yellow, orange, green and lilac"></div>
    <div class="panel">
      <div class="panel__emblem"></div>
      <h1 class="product-name">
        <span class="product-name__line">GOLDEN</span>
        <span class="product-name__line">RESERVE</span>
        <span class="product-name__script">Honey</span>
      </h1>
      <div class="jp-name">純粋はちみつ</div>
      <div class="tagline">
        <p>Rich taste &amp; Flavor</p>
        <p>It's made with pure selected</p>
        <p>loving honey</p>
      </div>
    </div>
  </section>
</main>
</body>
</html>
```